Hope KLN Disease (Non-Profit) Tri-Fold Brochure Design

We have put together the content for a brochure that we will distribute to doctors, researchers and patients about our non-profit. We would like the design of the brochure to look more professional and have nice aesthetics. It needs to incorporate all of the content in the attached Word file. We will have printed once we have a finished design.

Target Market(s)

Medical

Industry/Entity Type

Non Profit

Font styles to use
Serif
Sans Serif

Colors
33a6d7

Requirements
Must have
• Must include all content provided. Professional.
Nice to have
• Colors

```html
<!DOCTYPE html>
<html lang="en">
<head>
<meta charset="utf-8">
<title>Hope KLN Disease Tri-Fold Brochure</title>
<link rel="stylesheet" href="https://fonts.googleapis.com/css2?family=Montserrat:ital,wght@0,400;0,600;0,700;1,700&family=Roboto+Condensed:ital,wght@0,400;0,700;1,400&display=swap">
<style>
:root{
  --brand:#1a9ad6;
  --brand-soft:#33a6d7;
  --ink:#222;
  --grey:#555;
  --orange:#f39a2e;
  --orange-light:#f7b25a;
  --white:#fff;
}
*{margin:0;padding:0;box-sizing:border-box}
html,body{width:1200px;height:928px;overflow:hidden;background:#fff}
.brochure{position:relative;width:1200px;height:928px;font-family:"Roboto Condensed",Arial,sans-serif;color:var(--ink)}
.panel{position:absolute;top:0;width:400px;height:928px}
.panel--left{left:0}
.panel--mid{left:400px}
.panel--right{left:800px}
.header-photo{position:absolute;left:0;top:0;width:400px;height:157px}
.panel--left .header-photo{background:linear-gradient(100deg,#3f9fd8 0%,#6fc0ea 45%,#4aa6dc 100%)}
.panel--mid .header-photo{background:linear-gradient(180deg,#2f8fcf 0%,#5fb6e4 55%,#3a97d4 100%)}
.panel--right .header-photo{background:linear-gradient(80deg,#3a9bd8 0%,#78c6ec 55%,#4aa7dd 100%)}
.section-title{position:absolute;left:37px;top:99px;font-family:Montserrat,Arial,sans-serif;font-weight:700;font-size:26px;letter-spacing:1px;color:var(--white)}
.tagline{position:absolute;left:0;top:50px;width:400px;text-align:center;font-family:Montserrat,Arial,sans-serif;font-size:24px;line-height:26px;color:var(--white);letter-spacing:.5px}
.body{position:absolute;left:37px;width:327px;font-size:15.4px;line-height:18.8px;text-align:justify;color:var(--ink)}
.body p{margin-bottom:19px}
.term{color:var(--brand);font-weight:700}
.panel--left .body{top:202px}
.h2{font-family:Montserrat,Arial,sans-serif;font-weight:700;color:var(--brand);font-size:28px;letter-spacing:1px}
.research-title{position:absolute;left:35px;top:196px}
.research-text{position:absolute;left:36px;top:243px;width:328px;font-size:14.4px;line-height:17.5px;text-align:justify}
.callout{position:absolute;left:0;top:316px;width:400px;height:148px;background:var(--brand);color:var(--white);font-family:Montserrat,Arial,sans-serif;font-weight:700;font-size:20.5px;line-height:24px;text-align:center;padding:15px 30px 0;letter-spacing:.5px}
.goto{position:absolute;left:0;top:490px;width:400px;text-align:center;font-family:Montserrat,Arial,sans-serif;font-weight:600;font-size:22px;color:#555;letter-spacing:.5px}
.url-button{position:absolute;left:32px;top:534px;width:326px;height:43px;border-radius:9px;background:linear-gradient(180deg,#4aa9e6 0%,#1c7fcc 55%,#166fb8 100%);box-shadow:0 3px 5px rgba(0,0,0,.25);color:var(--white);font-family:Montserrat,Arial,sans-serif;font-size:27px;text-align:center;line-height:43px;letter-spacing:.5px}
.cursor{position:absolute;left:346px;top:568px}
.access{position:absolute;left:0;top:596px;width:400px;text-align:center;font-family:Montserrat,Arial,sans-serif;font-weight:600;font-size:22px;line-height:27px;color:#555;letter-spacing:.5px}
.registry-text{position:absolute;left:36px;top:683px;width:328px;font-size:15px;line-height:18.8px;text-align:justify}
.registry-text p{margin-bottom:19px}
.registry-strip{position:absolute;left:2px;top:845px;width:396px;height:53px;background:linear-gradient(90deg,#fff 0%,#f2f6fa 45%,#cfe0ee 70%,#e8f0f7 100%)}
.registry-name{position:absolute;left:7px;top:4px;font-family:"Roboto Condensed",Arial,sans-serif;font-size:18px;color:#1f4f86}
.registry-sub{position:absolute;left:8px;top:26px;font-size:8px;line-height:9px;color:#1f4f86}
.registry-globe{position:absolute;left:166px;top:2px;width:200px;height:51px;border-radius:100px 100px 0 0;background:radial-gradient(circle at 50% 100%,#c8dcec 0%,#a9c6df 60%,#e4eef6 100%)}
.panel--right .body{top:202px;width:328px}
.advisors{position:absolute;left:36px;top:337px;width:340px;display:flex;gap:14px}
.advisor{width:180px}
.advisor-name{font-family:Montserrat,Arial,sans-serif;font-weight:700;font-size:16.4px;color:var(--brand);white-space:nowrap}
.advisor-role{font-size:11.5px;font-weight:700;color:#666;margin-top:2px}
.advisor-place{font-size:11.5px;color:#666}
.advisor-mail{font-family:Montserrat,Arial,sans-serif;font-style:italic;font-size:12px;color:var(--brand)}
.protein-figure{position:absolute;left:85px;top:427px;width:230px;height:230px;border-radius:50%;background:radial-gradient(circle at 45% 50%,#1f6fc4 0%,#0d3a78 35%,#050a18 70%)}
.treat-title{position:absolute;left:36px;top:677px}
.treat-text{position:absolute;left:36px;top:717px;width:328px;font-size:15.4px;line-height:18.8px;text-align:justify}
.treat-text p{margin-bottom:19px}
.site-footer{position:absolute;right:36px;top:861px;font-family:Montserrat,Arial,sans-serif;font-weight:700;font-style:italic;font-size:17px;color:#333}
.base-band{position:absolute;left:0;top:899px;width:1200px;height:29px;background:linear-gradient(90deg,var(--orange) 0%,var(--orange-light) 20%,var(--orange) 33%,var(--orange-light) 53%,var(--orange) 66%,var(--orange-light) 86%,var(--orange) 100%)}
</style>
</head>
<body>
<main class="brochure">

  <section class="panel panel--left">
    <div class="header-photo" role="img" aria-label="Blue-toned laboratory photograph with test tubes"></div>
    <h2 class="section-title">SYMPTOMS</h2>
    <div class="body">
      <p>IMBPFD, a <i>KLN</i> Disease, is an adult onset disorder that can affect the muscles, bones, and brain, and an affected patient may have any combination of the following conditions:</p>
      <p><span class="term">Inclusion Body Myopathy:</span> The first symptom of IBMPFD is often muscle weakness (myopathy). Typically, patients first notice difficulty raising arms, losing balance or difficulty climbing stairs. As the disorder progresses, weakness develops in the other muscles in the arms, legs and core muscles. Muscle weakness can also affect respiratory and heart (cardiac) muscles. This disorder may first present in an individual's late 30's and over time occurs in approximately 90% of individuals with <i>KLN</i> Disease.</p>
      <p><span class="term">Pagets disease of bone:</span> Bone pain, particularly in the hips and spine, is usually the major symptom of Paget's disease. It most often affects bones of the hips, spine, and skull, and the long bones of the arms and legs. Paget's disease affects half of individuals with <i>KLN</i> Disease and typically first presents in a person's 30's or 40's, which is a much earlier age than those without <i>KLN</i> Disease.</p>
      <p><span class="term">Frontotemporal Dementia:</span> In about one-third of people with <i>KLN</i> Disease, the disorder also affects the brain. FTD may change personality, behaviour, language, and speech; but memory is preserved.</p>
      <p><span class="term">Amyotrophic Lateral Sclerosis (ALS or Lou Gehrig's disease):</span> ALS occurs in approximately 10% of individuals with <i>KLN</i> Disease. Symptoms include increased muscle tone, weakness, muscle wasting, muscle cramps, difficulty swallowing and speaking.</p>
    </div>
  </section>

  <section class="panel panel--mid">
    <div class="header-photo" role="img" aria-label="Blue-toned photograph of a researcher at a microscope"></div>
    <p class="tagline">Strength through numbers<br>will help US find a CURE!</p>
    <h2 class="h2 research-title">RESEARCH</h2>
    <p class="research-text">The goal of the RaLink registry is to connect as many patients and researchers as possible to help advance treatments and cures for rare diseases.</p>
    <div class="callout">If you have been diagnosed with IBMPFD or <i>KLN</i> Disease, please help us by completing the patient registry through RaLink.</div>
    <p class="goto">Go to our website</p>
    <div class="url-button">www.hopekln.org</div>
    <svg class="cursor" width="22" height="24" viewBox="0 0 22 24" aria-hidden="true"><path d="M2 2 L18 12 L11 13 L15 21 L12 22 L8 14 L3 18 Z" fill="#333" stroke="#fff" stroke-width="1"/></svg>
    <p class="access">to access the<br>RaLink Registry.</p>
    <div class="registry-text">
      <p>The RaLink registry is free for patients to enroll and for researchers to access.</p>
      <p>Please elect for researchers to have access to your registry, as that will greatly assist in the drive for a cure, especially when drug trials are recruiting patients.</p>
    </div>
    <div class="registry-strip">
      <span class="registry-name">RaLink Registry</span>
      <span class="registry-sub">Rare Disease Link<br>at Northfield</span>
      <div class="registry-globe" role="img" aria-label="Pale blue puzzle globe illustration"></div>
    </div>
  </section>

  <section class="panel panel--right">
    <div class="header-photo" role="img" aria-label="Blue-toned photograph of a clinician in a lab coat"></div>
    <h2 class="section-title">DIAGNOSIS</h2>
    <div class="body">
      <p>The only way of diagnosing <i>KLN</i> Disease is through genetic testing. Consult with your doctor about testing for mutations of the <i>KLN</i> gene.</p>
      <p>For information about genetic testing, our two medical advisors are available as resources:</p>
    </div>
    <div class="advisors">
      <div class="advisor">
        <div class="advisor-name">Dr. Helena Marlow</div>
        <div class="advisor-role">Medical Geneticist</div>
        <div class="advisor-place">at Westbrook University</div>
        <div class="advisor-mail">hmarlow@westbrook.edu</div>
      </div>
      <div class="advisor">
        <div class="advisor-name">Dr. Martin Osterby</div>
        <div class="advisor-role">Neuromuscular Specialist</div>
        <div class="advisor-place">at Eastlake University</div>
        <div class="advisor-mail">mosterby@eastlake.edu</div>
      </div>
    </div>
    <div class="protein-figure" role="img" aria-label="Ribbon model of the KLN protein structure showing its domains"></div>
    <h2 class="h2 treat-title">TREATMENTS:</h2>
    <div class="treat-text">
      <p>There is an approved treatment for Paget's disease of bone, so early testing for this disorder is very important.</p>
      <p>There are no known cures or treatments for the Inclusion Body Myopathy or Frontotemporal Dementia. Consult with your doctor about physical therapy, stretching, diet and mobility aids.</p>
    </div>
    <p class="site-footer">www.hopekln.org</p>
  </section>

  <div class="base-band"></div>
</main>
</body>
</html>
```